Interior Designer Branding Package

I need a full branding Package for print.
Business Card, Folder, Letter Head (Stationary) Note Pad, & Individual postcard type describing services, etc..
I also need a logo to add to a tote bag that will be part of my first initial client meeting.
I am an interior designer & furniture designer.
www.lumvarostudio.com
I have included some samples of what I am looking for & a sample of the tote bags I am thinking of embroidering the logo etc.. on the burlap portion.
Target Market(s)
High End -Full Interior Design Services: For Residential Customers
Industry/Entity Type
Business
Contact Information for Business Card
Company Name
Logo
Services-website-email-phone
Requirements
Nice to have
- Look sophisticated, bold, creative design

```html
<!DOCTYPE html>
<html lang="en">
<head>
<meta charset="utf-8">
<title>Lumvaro Studio — Business Card</title>
<link href="https://fonts.googleapis.com/css2?family=Didact+Gothic&family=Montserrat:wght@700&display=swap" rel="stylesheet">
<style>
  :root {
    --backdrop: #dcdee0;
    --card-white: #fbfbfb;
    --card-black: #262626;
    --ink: #1e1e1e;
    --ink-soft: #4a4a4a;
    --ink-reverse: #d9d9d9;
  }
  * { margin: 0; padding: 0; box-sizing: border-box; }
  html, body {
    width: 1200px; height: 966px; overflow: hidden;
    background: var(--backdrop);
  }
  .sheet {
    width: 1200px; height: 966px;
    display: flex; flex-direction: column;
    align-items: center; justify-content: center;
    gap: 56px;
  }
  .card {
    width: 600px; height: 343px;
    position: relative;
    box-shadow: 0 6px 18px rgba(0,0,0,0.12);
  }
  .card--back { background: var(--card-black); }
  .card--front { background: var(--card-white); }

  .wordmark {
    display: flex; align-items: center; gap: 14px;
    font-family: "Didact Gothic", sans-serif;
    text-transform: uppercase;
  }
  .wordmark__square {
    width: 34px; height: 34px;
  }
  .wordmark__name {
    font-size: 30px; line-height: 1; letter-spacing: 4px;
  }
  .card--back .wordmark {
    position: absolute; left: 50%; top: 50%;
    transform: translate(-50%, -50%);
    color: var(--ink-reverse);
  }
  .card--back .wordmark__square { background: var(--ink-reverse); }

  .card--front .wordmark {
    position: absolute; right: 44px; top: 118px;
    color: var(--ink);
  }
  .card--front .wordmark__square { background: var(--ink); }
  .card--front .wordmark__name { font-size: 26px; letter-spacing: 3px; }

  .contact {
    position: absolute; left: 40px; bottom: 48px;
    font-family: "Didact Gothic", sans-serif;
    color: var(--ink-soft);
  }
  .contact__name {
    font-family: "Montserrat", sans-serif; font-weight: 700;
    font-size: 15px; letter-spacing: 0.5px; color: var(--ink);
    text-transform: uppercase;
  }
  .contact__role { font-size: 12px; margin-top: 3px; margin-bottom: 14px; }
  .contact__line { font-size: 11.5px; line-height: 1.55; }
  .contact__label { font-family: "Montserrat", sans-serif; font-weight: 700; color: var(--ink); }
</style>
</head>
<body>
  <main class="sheet">
    <section class="card card--back" aria-label="Business card back">
      <div class="wordmark">
        <span class="wordmark__square"></span>
        <span class="wordmark__name">Lumvaro Studio</span>
      </div>
    </section>

    <section class="card card--front" aria-label="Business card front">
      <div class="wordmark">
        <span class="wordmark__square"></span>
        <span class="wordmark__name">Lumvaro Studio</span>
      </div>
      <div class="contact">
        <p class="contact__name">Elena Sofia Ravelli-Dunmore</p>
        <p class="contact__role">Furniture &amp; Interior Designer</p>
        <p class="contact__line"><span class="contact__label">M:</span> 555.014.2283 · <span class="contact__label">T:</span> 555.014.7310 · <span class="contact__label">F:</span> 555.014.9046</p>
        <p class="contact__line"><span class="contact__label">E:</span> elena@lumvarostudio.com · www.lumvarostudio.com</p>
      </div>
    </section>
  </main>
</body>
</html>
```